Menu Design, lay out and font to be professionally finished

We need a menu designed.

We need to have a similar font that is used in our logo. It is an old type writer font, we also have some flecks in it to make it look old. We would like this to be consistant throughout the menu.

We would need it to be formatted very professionally. We would like our logo used in the title of the menu.

The menu will be on A4 paper.

It would be preferable if the menu could be on a word document so it can be altered easily, Im not sure if we can get the required font through word?

We will require the winning designer to also complete a simple drinks menu in the same style as the food menu. This is included in the the project.

Requirements
Must have
• I just need the font to look like it was typed on an old type writer? I will print on old looking paper!

```html
<!DOCTYPE html>
<html lang="en">
<head>
<meta charset="utf-8">
<title>The Heron &amp; Oak – All Day Menu</title>
<link href="https://fonts.googleapis.com/css2?family=Special+Elite&display=swap" rel="stylesheet">
<style>
  :root {
    --paper: #ffffff;
    --ink: #1c1c1c;
    --ink-soft: #333333;
  }
  * { margin: 0; padding: 0; box-sizing: border-box; }
  html, body { width: 849px; height: 1200px; overflow: hidden; background: var(--paper); }
  body { font-family: "Special Elite", "Courier New", monospace; color: var(--ink); }
  .menu { position: relative; width: 849px; height: 1200px; padding: 40px 64px 0 64px; }
  .brand { text-align: center; font-size: 58px; font-weight: 400; letter-spacing: -1px; line-height: 1; margin-top: 8px; }
  .menu-title { text-align: center; font-size: 21px; font-weight: 400; margin-top: 20px; -webkit-text-stroke: 0.6px var(--ink); }
  .intro { text-align: center; font-size: 10.5px; line-height: 1.35; font-style: italic; margin-top: 10px; color: var(--ink-soft); }
  .items { list-style: none; margin-top: 24px; }
  .item { display: flex; justify-content: space-between; align-items: flex-start; font-size: 11px; line-height: 1.45; margin-bottom: 17px; }
  .item-desc { max-width: 520px; }
  .item-price { width: 40px; text-align: right; }
  .item-price span { display: block; }
  .section-title { font-size: 17px; margin-top: 30px; margin-bottom: 14px; -webkit-text-stroke: 0.5px var(--ink); }
  .rule { border: none; border-top: 1px solid var(--ink); width: 100%; margin-bottom: 12px; }
</style>
</head>
<body>
<main class="menu">
  <header>
    <h1 class="brand">the Heron &amp; Oak</h1>
    <h2 class="menu-title">All Day Menu</h2>
    <p class="intro">At The Heron &amp; Oak all our eggs are organic.<br>
      Our meat is free range &amp; organic where possible.<br>
      Breads are sourdough, baked daily by Ollie.<br>
      See front counter for daily sweet selection.</p>
  </header>

  <ul class="items">
    <li class="item"><span class="item-desc">Ollie's toasted sourdough with house made butter &amp; spreads<br>(gluten free also available)</span><span class="item-price">$6</span></li>
    <li class="item"><span class="item-desc">Our granola with Earl Grey figs, yogurt &amp; Granny Smith slaw</span><span class="item-price">$10</span></li>
    <li class="item"><span class="item-desc">Buckwheat and quinoa porridge with poached red fruits and<br>coconut caramel</span><span class="item-price">$10</span></li>
    <li class="item"><span class="item-desc">Two poached eggs on sourdough with smoked tomato relish</span><span class="item-price">$10</span></li>
    <li class="item"><span class="item-desc">Sides: Heart tomato, field mushroom, avocado, feta<br>Bacon, pork sausage, smoked salmon</span><span class="item-price"><span>$4</span><span>$5</span></span></li>
    <li class="item"><span class="item-desc">Bacon and egg roll – two fried organic eggs, bacon, caramelised onion,<br>slaw &amp; espresso bbq sauce</span><span class="item-price">$10</span></li>
    <li class="item"><span class="item-desc">Smashed avocado on toast with broad beans, mint and feta</span><span class="item-price">$15</span></li>
    <li class="item"><span class="item-desc">Smoked Harbour salmon on toast with house made labne, pickled fennel<br>and roe</span><span class="item-price">$15</span></li>
    <li class="item"><span class="item-desc">Clearwater River steak sandwich with burnt onions, smoked mozzarella,<br>lettuce, tomato, pickles &amp; mayo</span><span class="item-price">$15</span></li>
    <li class="item"><span class="item-desc">Salad of asparagus, broad beans &amp; zucchini with green wheat &amp;<br>sesame yogurt</span><span class="item-price">$16.5</span></li>
    <li class="item"><span class="item-desc">Heron's Big Breakfast<br>Pork sausage, bacon, fried eggs, roast tomato, field mushrooms &amp;<br>house beans with sourdough toast</span><span class="item-price">$19</span></li>
    <li class="item"><span class="item-desc">Bowl of sweet potato chips with pink river salt &amp; aioli</span><span class="item-price">$8</span></li>
  </ul>

  <section class="kids">
    <h3 class="section-title">Kids Meal</h3>
    <hr class="rule">
    <ul class="items" style="margin-top:0">
      <li class="item"><span class="item-desc">Little sausage sandwich plus a treat for later if they eat their peas :)</span><span class="item-price">$8</span></li>
      <li class="item"><span class="item-desc">Seasonal fruit cup with choc hazelnut spread for dipping</span><span class="item-price">$5</span></li>
    </ul>
  </section>
</main>
</body>
</html>
```